Box and label design for oil Tincture bottle

I need to design an attractive looking label for a 30ml CBD oil tincture along with designing a box for the tincture oil. I already have the logo (see attachment). I just need a nice, attractive looking artwork for the label and the box. The box is the standard 30ml tincture oil (see example attachment). The box has a total of 6 sides (4 on sides and 2 for top and bottom). Please include a section for supplemental facts and ingredients. Let's not focus to much on content. I am more concerned with design of box and label.
Target Market(s)
CBD customers
Look and feel
Each slider illustrates characteristics of the customer's brand and the style your logo design should communicate.

```html
<!DOCTYPE html>
<html lang="en">
<head>
<meta charset="utf-8">
<title>Clear Meadow – Tincture Label and Box</title>
<link href="https://fonts.googleapis.com/css2?family=Montserrat:wght@400;600;700&family=Oswald:wght@500&family=Roboto:wght@400;700;900&display=swap" rel="stylesheet">
<style>
  :root{
    --bg:#eceef0;
    --navy:#1b3d8c;
    --blue:#2a62b8;
    --ink:#1e2a44;
    --ice:#eef7fc;
    --sky:#cfe7f6;
    --deep-sky:#9fcdec;
    --white:#ffffff;
  }
  *{box-sizing:border-box;margin:0;padding:0}
  html,body{width:1200px;height:960px;overflow:hidden;background:var(--bg)}
  body{position:relative;font-family:"Montserrat",Arial,sans-serif;color:var(--navy)}

  .panel{position:absolute;background:linear-gradient(180deg,var(--white) 0%,var(--ice) 35%,var(--sky) 75%,var(--deep-sky) 100%);box-shadow:0 2px 6px rgba(0,0,0,.08);overflow:hidden}
  .panel__column{position:absolute;top:0;bottom:0;background:rgba(255,255,255,.55)}
  .artwork{position:absolute;background:linear-gradient(180deg,rgba(159,205,236,0) 0%,rgba(120,185,230,.55) 100%)}

  .brand{position:absolute;left:0;right:0;display:flex;align-items:center;justify-content:center;gap:7px}
  .brand__dot{border-radius:50%;background:var(--navy);flex:none}
  .brand__name{font-family:"Montserrat",Arial,sans-serif;font-weight:700;color:var(--navy);line-height:1;white-space:nowrap}

  .title{text-align:center;color:var(--navy);line-height:1.05}
  .title b{font-weight:700}
  .title span{font-weight:400}
  .natural{display:flex;align-items:center;justify-content:center;gap:8px;color:var(--blue);font-weight:400}
  .natural::before,.natural::after{content:"";height:1px;width:30px;background:var(--blue)}
  .condensed{font-family:"Oswald",Arial Narrow,sans-serif;font-weight:500}

  .dose{text-align:center;color:var(--ink);line-height:1.35}
  .site{position:absolute;font-family:"Oswald",Arial Narrow,sans-serif;font-weight:500;font-size:11px;color:var(--navy);white-space:nowrap}

  .label{left:40px;top:330px;width:230px;height:340px}
  .label .panel__column{left:34px;right:34px;top:130px;bottom:22px;background:rgba(255,255,255,.75)}

  .side-a{left:300px;top:140px;width:160px;height:680px}
  .front{left:460px;top:140px;width:270px;height:680px}
  .side-b{left:730px;top:140px;width:160px;height:680px}
  .back{left:890px;top:140px;width:270px;height:680px}

  .front .panel__column{left:28px;right:28px;top:200px;bottom:12px;border-bottom:2px solid var(--blue)}
  .back .panel__column{left:22px;right:22px;top:0;bottom:12px;background:rgba(255,255,255,.8);border-bottom:2px solid var(--blue)}

  .facts{position:absolute;left:34px;right:34px;top:390px;background:var(--white);border:1.5px solid var(--ink);padding:6px 7px;font-family:"Roboto",Arial,sans-serif;color:var(--ink);font-size:9.5px}
  .facts__head{font-weight:900;font-size:17px;line-height:1}
  .facts__meta{font-size:9.5px;line-height:1.15;border-bottom:5px solid var(--ink);padding-bottom:3px;margin-bottom:2px}
  .facts table{width:100%;border-collapse:collapse}
  .facts th{font-weight:700;text-align:right;font-size:9.5px;line-height:1.1;padding-bottom:2px;border-bottom:2px solid var(--ink)}
  .facts td{padding:2px 0;border-bottom:1px solid var(--ink);vertical-align:top}
  .facts td.num{text-align:center}
  .facts td.dv{text-align:right}
  .facts tr.last td{border-bottom:3px solid var(--ink)}
  .facts__notes{font-size:9.5px;line-height:1.25;padding-top:4px}
</style>
</head>
<body>

<section class="panel label">
  <div class="artwork" style="left:0;right:0;top:160px;bottom:0" role="img" aria-label="Soft light-blue field rows and sprout artwork"></div>
  <div class="panel__column"></div>
  <div class="brand" style="top:80px"><span class="brand__dot" style="width:12px;height:12px"></span><span class="brand__name" style="font-size:19px">Clear Meadow</span></div>
  <div style="position:absolute;top:150px;left:0;right:0">
    <p class="title" style="font-size:27px"><b>CBD</b> <span>oil</span><br><span>tincture</span></p>
    <p class="natural" style="font-size:12px;margin-top:4px">Natural</p>
    <p class="dose" style="font-size:12px;margin-top:18px">30ml<br>250mg CBD</p>
  </div>
</section>

<section class="panel side-a">
  <div class="artwork" style="left:0;right:0;top:380px;bottom:0" role="img" aria-label="Soft light-blue field rows artwork"></div>
  <div class="brand" style="top:285px"><span class="brand__dot" style="width:8px;height:8px"></span><span class="brand__name" style="font-size:13px">Clear Meadow</span></div>
  <div style="position:absolute;top:330px;left:0;right:0">
    <p class="title condensed" style="font-size:30px">CBD oil<br>tincture</p>
    <p class="natural condensed" style="font-size:12px;margin-top:4px">Natural</p>
  </div>
  <p class="site" style="left:16px;bottom:30px">www.clearmeadowcbd.com</p>
</section>

<section class="panel front">
  <div class="artwork" style="left:0;right:0;top:330px;bottom:0" role="img" aria-label="Sprouting plant over curved field rows in pale blue"></div>
  <div class="panel__column"></div>
  <div class="brand" style="top:135px"><span class="brand__dot" style="width:16px;height:16px"></span><span class="brand__name" style="font-size:26px">Clear Meadow</span></div>
  <div style="position:absolute;top:260px;left:0;right:0">
    <p class="title" style="font-size:37px"><b>CBD</b> <span>oil</span><br><span>tincture</span></p>
    <p class="natural" style="font-size:17px;margin-top:6px">Natural</p>
  </div>
  <p class="dose" style="position:absolute;left:0;right:0;bottom:42px;font-size:21px;line-height:1.6">30ml<br>250mg CBD</p>
</section>

<section class="panel side-b">
  <div class="artwork" style="left:0;right:0;top:380px;bottom:0" role="img" aria-label="Soft light-blue field rows artwork"></div>
  <div class="brand" style="top:285px"><span class="brand__dot" style="width:8px;height:8px"></span><span class="brand__name" style="font-size:13px">Clear Meadow</span></div>
  <div style="position:absolute;top:330px;left:0;right:0">
    <p class="title condensed" style="font-size:30px">CBD oil<br>tincture</p>
    <p class="natural condensed" style="font-size:12px;margin-top:4px">Natural</p>
  </div>
  <p class="site" style="left:16px;bottom:30px">www.clearmeadowcbd.com</p>
</section>

<section class="panel back">
  <div class="panel__column"></div>
  <div class="brand" style="top:80px"><span class="brand__dot" style="width:10px;height:10px"></span><span class="brand__name" style="font-size:16px">Clear Meadow</span></div>
  <div style="position:absolute;top:145px;left:0;right:0">
    <p class="title" style="font-size:26px"><b>CBD</b> <span>oil</span><br><span>tincture</span></p>
    <p class="natural" style="font-size:12px;margin-top:4px">Natural</p>
  </div>
  <p style="position:absolute;left:36px;right:30px;top:275px;font-size:13px;line-height:1.35;color:var(--blue)">Our premium quality Full Spectrum Oil Tinctures are infused with rich cannabinoids which include CBD, CBDV, and CBG.</p>

  <div class="facts">
    <p class="facts__head">Supplement Facts</p>
    <p class="facts__meta">Serving Size: 1/2 dropper (0.5 mL)<br>Servings Per Container: 200</p>
    <table>
      <tr><th></th><th style="text-align:center">Amount Per<br>Serving</th><th>% Daily<br>Value</th></tr>
      <tr><td>Calories</td><td class="num">5</td><td class="dv"></td></tr>
      <tr><td>Total Fat</td><td class="num">0.5 g</td><td class="dv">1%*</td></tr>
      <tr class="last"><td>Hemp Extract<br>(aerial parts)</td><td class="num">43 mg</td><td class="dv">**</td></tr>
    </table>
    <p class="facts__notes">*Percent Daily Values (DV) are based on a 2,000 calorie diet.<br>**Daily Value (DV) not established.</p>
  </div>

  <p style="position:absolute;left:36px;right:30px;bottom:40px;font-family:'Roboto',Arial,sans-serif;font-size:11.5px;line-height:1.35;color:var(--ink)">SUGGESTED USE<br>ADULTS TAKE 1/2 DROPPER<br>(0.5 mL) 2-3 TIMES PER DAY.</p>
</section>

</body>
</html>
```